Building Servicess

We need a new business card design for a company. We specialise in: Electrical/Site temporary electrics, Data/Network Installation, Passive Fire Protection

Industry/Entity Type

Construction

Contact Information for Business Card

Services provided as detailed on project description

Font styles to use
Serif

Colors
0054AA
0677BA
7BADD7
CADEEF
E8F1F8
00AB8E
00BBA5
67D7C9
C6EFE9
E9F9F6
EB3D1F
EC4F4E
F09395
F8D3D4
FCEDEE

Requirements
Must have
• Company logo-contact details-phone numbers

```html
<!DOCTYPE html>
<html lang="en">
<head>
<meta charset="utf-8">
<title>Northgate Services – Business Card</title>
<link rel="stylesheet" href="https://fonts.googleapis.com/css2?family=Montserrat:wght@500;700&family=Arimo:wght@400&display=swap">
<style>
  :root {
    --page: #e4e4e2;
    --card: #333333;
    --card-deep: #161616;
    --card-mid: #5a5a5a;
    --blue: #0677ba;
    --white: #ffffff;
    --rule: #6b6b6b;
  }
  * { margin: 0; padding: 0; box-sizing: border-box; }
  html, body { width: 1200px; height: 801px; overflow: hidden; }
  body {
    background: var(--page);
    font-family: "Arimo", Arial, sans-serif;
    position: relative;
  }
  .card {
    position: absolute;
    top: 245px;
    width: 540px;
    height: 310px;
    background: var(--card);
    border-bottom: 4px solid var(--blue);
    box-shadow: 0 10px 24px rgba(0,0,0,0.18);
    overflow: hidden;
  }
  .card--front { left: 40px; }
  .card--back { left: 620px; }

  /* front */
  .brand {
    position: absolute;
    left: 36px;
    top: 52px;
    width: 262px;
  }
  .brand__row { display: flex; align-items: center; gap: 9px; }
  .brand__mark {
    width: 24px; height: 24px;
    background: var(--blue);
    flex: none;
  }
  .brand__name {
    font-family: "Montserrat", Arial, sans-serif;
    font-weight: 700;
    font-size: 17px;
    letter-spacing: 0.3px;
    color: var(--blue);
    white-space: nowrap;
  }
  .brand__suffix {
    font-family: "Montserrat", Arial, sans-serif;
    font-weight: 500;
    font-size: 9px;
    letter-spacing: 5px;
    color: var(--white);
    text-align: right;
    margin-top: 4px;
  }
  .brand__rule {
    height: 1.5px;
    background: var(--white);
    margin-top: 6px;
  }
  .person {
    position: absolute;
    left: 36px;
    top: 160px;
  }
  .person__name {
    font-family: "Montserrat", Arial, sans-serif;
    font-weight: 700;
    font-size: 22px;
    color: var(--blue);
  }
  .person__role {
    font-size: 14px;
    color: var(--white);
    margin-top: 3px;
    padding-left: 60px;
  }
  .divider {
    position: absolute;
    left: 318px;
    top: 52px;
    width: 1px;
    height: 150px;
    background: var(--rule);
  }
  .contacts {
    position: absolute;
    left: 338px;
    top: 60px;
    list-style: none;
  }
  .contacts li {
    display: flex;
    align-items: center;
    gap: 9px;
    font-size: 13px;
    color: var(--white);
    margin-bottom: 11px;
    white-space: nowrap;
  }
  .contacts svg { width: 13px; height: 13px; flex: none; }
  .accent { color: var(--blue); }
  .address {
    position: absolute;
    left: 210px;
    top: 240px;
    font-size: 14px;
    color: var(--white);
  }

  /* back */
  .back__pattern {
    position: absolute;
    left: 0; top: 0;
    width: 400px; height: 100%;
    background: linear-gradient(115deg, var(--card-deep) 0%, var(--card) 40%, var(--card-mid) 70%, var(--card) 100%);
  }
  .back__brand {
    position: absolute;
    left: 425px;
    top: 30px;
    width: 250px;
    height: 70px;
    transform-origin: 0 0;
    transform: rotate(-90deg) translate(-250px, 0);
  }
  .back__name {
    font-family: "Montserrat", Arial, sans-serif;
    font-weight: 700;
    font-size: 20px;
    color: var(--blue);
    white-space: nowrap;
  }
  .back__suffix {
    font-family: "Montserrat", Arial, sans-serif;
    font-weight: 500;
    font-size: 9px;
    letter-spacing: 5px;
    color: var(--white);
    text-align: right;
    margin-top: 3px;
  }
  .back__rule { height: 1.5px; background: var(--white); margin-top: 6px; }
</style>
</head>
<body>

<section class="card card--front">
  <div class="brand">
    <div class="brand__row">
      <span class="brand__mark"></span>
      <span class="brand__name">NORTHGATE SERVICES</span>
    </div>
    <div class="brand__suffix">LTD</div>
    <div class="brand__rule"></div>
  </div>

  <div class="person">
    <div class="person__name">Daniel Harper</div>
    <div class="person__role">Manager</div>
  </div>

  <div class="divider"></div>

  <ul class="contacts">
    <li>
      <svg viewBox="0 0 24 24" aria-hidden="true"><path fill="#0677ba" d="M6.6 10.8a15 15 0 0 0 6.6 6.6l2.2-2.2c.3-.3.7-.4 1-.2 1.1.4 2.3.6 3.6.6.6 0 1 .4 1 1V20c0 .6-.4 1-1 1A17 17 0 0 1 3 4c0-.6.4-1 1-1h3.5c.6 0 1 .4 1 1 0 1.3.2 2.5.6 3.6.1.3 0 .7-.2 1z"/></svg>
      555-018-2100
    </li>
    <li>
      <svg viewBox="0 0 24 24" aria-hidden="true"><path fill="#0677ba" d="M2 5h20v14H2z"/><path fill="none" stroke="#333" stroke-width="1.8" d="M2 5l10 8 10-8"/></svg>
      info@northgatesite.co
    </li>
    <li>
      <svg viewBox="0 0 24 24" aria-hidden="true"><circle cx="12" cy="12" r="10" fill="#0677ba"/><path fill="none" stroke="#333" stroke-width="1.5" d="M2 12h20M12 2c3 3 3 17 0 20M12 2c-3 3-3 17 0 20"/></svg>
      <span>www.<span class="accent">northgatesite</span>.co</span>
    </li>
  </ul>

  <p class="address">14 Mill Road, Ashford, KT 0000</p>
</section>

<section class="card card--back">
  <div class="back__pattern" role="img" aria-label="Large faint brand symbol in layered grey tones"></div>
  <div class="back__brand">
    <div class="back__name">NORTHGATE SERVICES</div>
    <div class="back__suffix">LTD</div>
    <div class="back__rule"></div>
  </div>
</section>

</body>
</html>
```